依頼詳細
依頼詳細下記となります。
(1)を一番強調し、(2)の2つは同じ扱いでお願いします。

-------------------------------------------------------------------------------------------------

(1)
ハルネ管理物件内での住み替えは

仲介手数料0円!!(これを特に強調)

(2)
その他にも

[購入を検討のお客さま]
ハルネ管理物件にご入居中のお客さまがハルネで売買物件を購入された場合
仲介手数料10%引き!

[他のエリアに住み替え検討のお客さま]
松江や米子はもちろん全国のお部屋探しもサポートさせて頂きます。
お気軽にご相談ください!

他に必要なキャッチ等あれば入れて頂いてかまいません。
記載項目
抑え※添付ファイル参照
サイズ
A4
ページ数
片面
希望イメージ
シンプル 複雑
単色 カラフル
暗い 明るい
日常 高級
遊び心 厳粛
未来的 伝統的
女性的 男性的
希望する色
水色系、緑系、グレー系、弊社のホームページの色調(グレー、青緑?)
納品ファイル
• イラストレーター形式 (.ai)
補足説明
■ 選んだ理由

社員全員による投票で決定しました。

■ 提案者全員のお礼・コメント

素敵な提案ありがとうございました。

また修正依頼にも迅速に対応頂き感謝します。

また機会がありましたらよろしくお願いします。

```html
<!DOCTYPE html>
<html lang="ja">
<head>
<meta charset="utf-8">
<title>ハルネ管理物件ご入居者様限定特典</title>
<link href="https://fonts.googleapis.com/css2?family=M+PLUS+Rounded+1c:wght@500;800;900&family=Noto+Sans+JP:wght@400;700;900&display=swap" rel="stylesheet">
<style>
:root{
  --teal:#4fb9bd;
  --teal-deep:#1f8f95;
  --teal-dark:#16666b;
  --navy:#1d3f5c;
  --white:#ffffff;
  --ink:#2b3a40;
  --grey:#5a6770;
  --pale:#e9f6f6;
}
*{margin:0;padding:0;box-sizing:border-box}
html,body{width:848px;height:1200px;overflow:hidden;background:var(--white)}
body{font-family:"Noto Sans JP",sans-serif;color:var(--ink)}
.poster{position:relative;width:848px;height:1200px;background:var(--teal);overflow:hidden}
.top-band{position:absolute;left:0;top:0;width:100%;height:54px;background:var(--teal-dark);color:var(--white);
  font-weight:700;font-size:28px;letter-spacing:3px;text-align:center;line-height:54px;z-index:5}
.skyline{position:absolute;left:0;top:54px;width:100%;height:420px;
  background:linear-gradient(180deg,var(--teal) 0%,#7fd0d0 70%,var(--teal) 100%);opacity:.9}
.circle{position:absolute;border-radius:50%;background:var(--white)}
.main-circle{left:134px;top:96px;width:580px;height:580px}
.hero{position:absolute;left:0;top:0;width:100%;height:100%;z-index:2}
.main-lead{position:absolute;top:148px;width:100%;text-align:center;font-weight:900;font-size:32px;line-height:1.2;color:var(--navy)}
.main-sub{position:absolute;top:196px;width:100%;text-align:center;font-weight:900;font-size:56px;line-height:1.2;color:var(--navy)}
.main-sub span{font-size:44px}
.main-rule{position:absolute;left:300px;width:248px;top:270px;height:4px;background:var(--teal)}
.zero{position:absolute;left:0;width:100%;top:262px;text-align:center;font-family:"M PLUS Rounded 1c",sans-serif;font-weight:900;
  font-size:250px;line-height:1;color:var(--teal-dark)}
.fee-label{position:absolute;left:186px;top:392px;width:150px;font-weight:900;font-size:44px;line-height:1.15;color:var(--teal-deep);text-align:center}
.yen{position:absolute;left:548px;top:446px;font-weight:900;font-size:60px;line-height:1.2;color:var(--teal-deep)}
.art-family{position:absolute;left:190px;top:288px;width:140px;height:92px;border-radius:14px;background:linear-gradient(180deg,#f3d9c4,#b9dfe0)}
.art-staff{position:absolute;left:562px;top:288px;width:104px;height:150px;border-radius:14px;background:linear-gradient(180deg,#f3d9c4,#8fb5c9)}
.other-circle{left:348px;top:622px;width:152px;height:152px;background:var(--pale);border:5px solid var(--white);z-index:4;
  display:flex;align-items:center;justify-content:center;text-align:center;font-weight:900;font-size:28px;line-height:1.25;color:var(--teal-dark)}
.offer{position:absolute;top:660px;width:396px;height:396px;z-index:1}
.offer-left{left:14px}
.offer-right{left:438px}
.offer-head{position:absolute;top:44px;height:90px;background:var(--teal-deep);color:var(--white);border-radius:45px;
  display:flex;align-items:center;justify-content:center;text-align:center;font-weight:900;font-size:25px;line-height:1.3}
.offer-left .offer-head{left:36px;right:64px}
.offer-right .offer-head{left:64px;right:36px}
.offer-body{position:absolute;top:150px;left:40px;right:40px;text-align:center}
.offer-note{font-size:17px;line-height:1.45;color:var(--grey)}
.offer-strong{font-weight:900;font-size:32px;line-height:1.3;color:var(--teal-deep);margin-top:6px}
.offer-big{font-weight:900;font-size:70px;line-height:1.1;color:var(--teal-deep)}
.offer-big small{font-size:38px}
.offer-lead{font-weight:700;font-size:20px;line-height:1.4;color:var(--navy)}
.offer-em{font-weight:900;font-size:31px;line-height:1.3;color:var(--teal-deep)}
.offer-em2{font-weight:900;font-size:25px;line-height:1.4;color:var(--navy)}
.offer-small{font-size:16px;color:var(--grey);margin-top:4px}
.art-couple{position:absolute;left:374px;top:830px;width:100px;height:180px;border-radius:18px;background:linear-gradient(180deg,#cfe9ea,#8fcfd0);z-index:2}
.catch{position:absolute;left:0;top:1020px;width:100%;height:64px;background:var(--white);display:flex;align-items:center;padding-left:30px;gap:12px;z-index:5}
.catch small{font-size:15px;font-weight:700;color:var(--teal-deep);background:var(--pale);padding:3px 8px;border-radius:4px;white-space:nowrap}
.catch strong{font-weight:900;font-size:32px;color:var(--navy);border-bottom:4px solid var(--teal);white-space:nowrap}
.footer{position:absolute;left:0;top:1096px;width:100%;height:104px;background:var(--white);border-top:3px solid var(--teal);
  display:flex;align-items:center;padding:0 26px;gap:22px;z-index:5}
.brand{display:flex;align-items:center;gap:8px;font-weight:900;font-size:22px;color:var(--navy)}
.brand i{display:block;width:18px;height:18px;background:var(--navy)}
.brand.company i{border-radius:50%;background:var(--teal-deep)}
.brand.company{color:var(--teal-deep)}
.contact{margin-left:auto;text-align:left}
.tel{display:flex;align-items:center;gap:8px;font-weight:900;font-size:34px;color:var(--navy)}
.tel span{font-size:18px}
.address{font-size:11px;color:var(--grey);line-height:1.4}
</style>
</head>
<body>
<div class="poster">
  <div class="top-band">ハルネ管理物件ご入居者様限定特典</div>
  <div class="skyline" role="img" aria-label="淡い水色の街並みのイラスト"></div>

  <div class="circle main-circle"></div>
  <div class="hero">
    <p class="main-lead">ハルネ管理物件内での</p>
    <p class="main-sub">住み替え<span>は</span></p>
    <div class="main-rule"></div>
    <div class="art-family" role="img" aria-label="家族のイラスト"></div>
    <div class="art-staff" role="img" aria-label="スーツ姿の担当者のイラスト"></div>
    <div class="zero">0</div>
    <p class="fee-label">仲介<br>手数料</p>
    <p class="yen">円!!</p>
  </div>

  <div class="circle other-circle">その他<br>にも</div>

  <section class="circle offer offer-left">
    <h2 class="offer-head">ご購入を<br>検討のお客様</h2>
    <div class="offer-body">
      <p class="offer-note">ハルネ管理物件にご入居中のお客様が<br>ハルネで売買物件を購入された場合</p>
      <p class="offer-strong">仲介手数料</p>
      <p class="offer-big">10<small>%引き!</small></p>
    </div>
  </section>

  <section class="circle offer offer-right">
    <h2 class="offer-head">他のエリアに<br>住み替え検討のお客様</h2>
    <div class="offer-body">
      <p class="offer-lead">松江や米子はもちろん</p>
      <p class="offer-em">全国のお部屋探しも<br>サポート</p>
      <p class="offer-em2">させて頂きます。</p>
      <p class="offer-small">お気軽にご相談ください!</p>
    </div>
  </section>

  <div class="art-couple" role="img" aria-label="ソファでくつろぐ二人のイラスト"></div>

  <div class="catch">
    <small>これからも</small>
    <strong>住まいの事ならハルネにお任せください!!</strong>
  </div>

  <footer class="footer">
    <div class="brand"><i></i>ルームプラザ</div>
    <div class="brand company"><i></i>HARUNE</div>
    <div class="contact">
      <p class="tel"><span>TEL</span>0854-00-1234</p>
      <p class="address">〒000-0000 島根県サンプル市中央町1-2-3 株式会社ハルネ<br>www.harune-home.jp</p>
    </div>
  </footer>
</div>
</body>
</html>
```